Action Camera Rental Website, with add on video editing service

I'm looking for a new website, which I will be able to administer once complete which will list camera equipment for rental. There are some key features I would like which I have not been able to add on any proprietary site builders (see brief, reference to availability and booking system)
The website must have functionality to select products and check availability for their hire / rental. I would like the functionality to specify (for example), hire from 2nd to 9th, then the equipment arrival date will be 1st, return date will be 10th. See brief for link to similar page.
Website should be simple and quick to use.It should include FAQ page, to allow me to modify with questions . answers to limit the amount of questions I have to answer via email. I would also like a blog page to post videos made by or for our users.
I would also be interested in the functionality for users to upload their footage to a FTP site (or similar) for us to edit.

Target Market(s)

Young, adventurous people/ Action sports, holiday companies

Industry/Entity Type

Videography

Number of Pages Required

5+ page

Requirements
Must have
• Hire / Booking page, which checks availability of selected equipment. Be modifiable by me. Ability to add new products without needing support
Nice to have
• Vibrant, adventurous layout and colour scheme.

```html
<!DOCTYPE html>
<html lang="en">
<head>
<meta charset="utf-8">
<title>Rove Reel – Rent Anytime</title>
<link href="https://fonts.googleapis.com/css2?family=Arimo:wght@400;700&family=Permanent+Marker&display=swap" rel="stylesheet">
<style>
:root{
  --teal:#5aa3ad;
  --teal-dark:#16958f;
  --tan:#b98d55;
  --ink:#111;
  --grey-text:#666;
  --panel:#efefef;
  --plum:#a8558a;
  --black:#000;
  --white:#fff;
}
*{box-sizing:border-box;margin:0;padding:0}
html,body{width:1200px;height:3214px;overflow:hidden}
body{position:relative;font-family:Arimo,Arial,sans-serif;color:var(--ink);background:var(--white)}
.abs{position:absolute}
a{color:inherit;text-decoration:none}

/* top bar */
.topbar{left:0;top:0;width:1200px;height:38px;background:var(--black);color:#fff;font-size:13px}
.topbar .follow{left:79px;top:12px;display:flex;gap:12px;align-items:center}
.topbar .account{right:78px;top:12px;display:flex;gap:34px}
.dot{width:12px;height:12px;border-radius:50%;background:var(--teal);display:inline-block}

/* hero */
.hero{left:0;top:38px;width:1200px;height:637px;background:linear-gradient(180deg,#4d3a3a,#5b6f78 60%,#3c5560);overflow:hidden}
.stripes{position:absolute;inset:0;display:flex}
.stripes span{flex:1;opacity:.72}
.nav-band{left:0;top:0;width:1200px;height:97px;background:rgba(255,255,255,.12)}
.brand{left:77px;top:26px;font-size:38px;color:#fff}
.nav{left:440px;top:30px;display:flex;align-items:center;font-size:16px;color:#fff}
.nav a{margin-right:40px}
.nav .active{background:var(--teal);border-radius:22px;padding:12px 26px;margin-right:30px}
.hero-title{left:0;width:1200px;top:190px;text-align:center;color:#fff;font-family:'Permanent Marker',cursive;font-size:96px;line-height:1}
.hero-sub{left:0;width:1200px;top:305px;text-align:center;color:#fff;font-family:'Permanent Marker',cursive;font-size:44px}
.hero-tag{left:0;width:1200px;top:377px;text-align:center;font-size:22px;font-weight:700;color:#000}
.search{left:315px;top:433px;width:570px;height:56px;background:#fff;display:flex}
.search span{flex:1;padding:19px 16px;font-size:14px;color:#333}
.search b{width:56px;background:#111;display:flex;align-items:center;justify-content:center}

/* welcome */
.section-title{left:0;width:1200px;text-align:center;font-size:40px}
.section-title em{font-style:normal;color:var(--teal)}
.section-desc{left:230px;width:740px;text-align:center;font-size:14px;line-height:26px;color:var(--grey-text)}
.tile{top:885px;width:251px;height:270px;background:#e8e8e8}
.tile-art{position:absolute;left:40px;top:30px;width:171px;height:210px;border-radius:10px}
.chev{font-size:40px;color:#999;top:990px;font-weight:300}

/* shop */
.shop{left:0;top:1217px;width:1200px;height:830px;background:linear-gradient(90deg,var(--tan),#6f8c72 50%,var(--teal-dark))}
.shop .section-title,.shop .section-desc{color:#fff}
.card{left:184px;top:195px;width:832px;height:405px;background:var(--panel)}
.card-img{left:0;top:0;width:416px;height:405px;background:#fff}
.card-img div{position:absolute;left:78px;top:110px;width:260px;height:185px;border-radius:20px;background:radial-gradient(#555,#111)}
.pname{left:442px;top:30px;color:var(--teal);font-size:20px}
.stars{left:442px;top:62px;color:var(--teal);font-size:16px;letter-spacing:2px}
.price{left:442px;top:100px;font-size:26px;font-weight:700}
.pdesc{left:442px;top:152px;width:360px;font-size:14px;line-height:26px;color:#555}
.field{height:35px;background:#fff;border:1px solid #ddd;font-size:13px;color:#666;padding:10px 12px}
.book{left:442px;top:315px;width:175px;height:56px;border-radius:28px;background:var(--teal);color:#fff;font-size:18px;text-align:center;line-height:56px}
.thumb{top:611px;width:156px;height:154px;background:#fff}
.thumb div{position:absolute;inset:25px;border-radius:8px}
.circle-arrow{top:667px;width:46px;height:46px;border:1.5px solid #fff;border-radius:50%}

/* blog */
.video{left:77px;top:2192px;width:677px;height:416px;background:#111}
.video-img{position:absolute;left:4px;top:4px;width:669px;height:370px;background:linear-gradient(160deg,#0e3f55,#2b7d93 45%,#cfe4e6 75%,#4a6d78)}
.vbtn{position:absolute;right:12px;width:40px;height:40px;background:#333;border:1px solid #777}
.post-img{left:774px;width:158px;height:105px;border:2px solid #222}
.post-text{left:954px;width:165px;font-size:14px;line-height:25px;color:var(--teal)}
.post-text span{color:#444}
.upload{left:771px;top:2554px;width:198px;height:56px;border-radius:28px;background:var(--teal);color:#fff;font-size:20px;text-align:center;line-height:56px}

/* newsletter */
.newsletter{left:0;top:2672px;width:1200px;height:195px;background:var(--plum);color:#fff}
.newsletter h2{position:absolute;left:79px;top:48px;font-size:38px;font-weight:400}
.newsletter p{position:absolute;left:79px;top:103px;width:340px;font-size:13px;line-height:22px}
.email{left:448px;top:71px;width:478px;height:60px;background:#fff;color:#888;font-size:14px;padding:22px 18px}
.subscribe{left:939px;top:71px;width:175px;height:60px;border-radius:30px;background:var(--teal);text-align:center;line-height:60px;font-size:20px}

/* footer */
.footer{left:0;top:2867px;width:1200px;height:283px;background:var(--black);color:#ccc}
.footer h4{position:absolute;top:30px;color:var(--teal);font-size:18px;font-weight:400}
.f-brand{left:79px;top:92px;font-size:38px;color:#fff}
.f-about{left:95px;top:146px;width:170px;text-align:center;font-size:13px;line-height:24px}
.f-links{left:345px;top:70px;list-style:none;font-size:14px;line-height:27.5px}
.f-links li::before{content:"»";color:var(--teal);margin-right:14px}
.f-post{left:611px;font-size:13px;line-height:24px;width:230px}
.f-post i{position:absolute;left:0;top:0;width:60px;height:60px;border-radius:50%;background:linear-gradient(#6b8fa8,#3a4a55)}
.f-post p{margin-left:73px}
.f-post small{color:var(--teal);font-size:13px}
.social{left:874px;display:flex;align-items:center;gap:20px;font-size:14px}
.social i{width:46px;height:46px;border-radius:50%;border:1.5px solid #888}
.social .on{background:var(--teal);border-color:var(--teal)}
.bottombar{left:0;top:3150px;width:1200px;height:64px;background:var(--teal);text-align:center;line-height:64px;font-size:14px;color:#222}
</style>
</head>
<body>

<header>
  <div class="abs topbar">
    <div class="abs follow">Follow Us : <i class="dot"></i><i class="dot"></i><i class="dot"></i></div>
    <div class="abs account"><span>🔒 My Account</span><span>🛒 My Cart</span></div>
  </div>

  <section class="abs hero">
    <div class="stripes" role="img" aria-label="Photo of a surfer riding a wave, tinted with vertical colour bands">
      <span style="background:#c3507a"></span><span style="background:#7a3a37"></span><span style="background:#d6a45a"></span><span style="background:#546a2d"></span><span style="background:#7ec0c4"></span><span style="background:#b35aa5"></span>
    </div>
    <div class="abs nav-band"></div>
    <div class="abs brand">Rove Reel</div>
    <nav class="abs nav">
      <a class="active">HOME</a><a>ABOUT US</a><a>SHOP</a><a>NEWS</a><a>FAQ</a><a>BLOG</a><a>CONTACT US</a>
    </nav>
    <h1 class="abs hero-title">Rent Anytime</h1>
    <div class="abs hero-sub">Rent Anywhere</div>
    <div class="abs hero-tag">Why Buy When You Can Rent</div>
    <div class="abs search"><span>Search.....</span><b><svg width="22" height="22" viewBox="0 0 22 22"><circle cx="9" cy="9" r="6.5" stroke="#5aa3ad" stroke-width="2.5" fill="none"/><line x1="14" y1="14" x2="20" y2="20" stroke="#5aa3ad" stroke-width="2.5"/></svg></b></div>
  </section>
</header>

<main>
  <h2 class="abs section-title" style="top:736px">Welcome To <em>Rove Reel</em></h2>
  <p class="abs section-desc" style="top:798px">COMPANY NAME has been delivering results since we opened in YEAR. Our goal is to provide both a superior customer experience and tremendous value for our customers.</p>
  <span class="abs chev" style="left:32px">‹</span>
  <div class="abs tile" style="left:77px"><div class="tile-art" role="img" aria-label="Grey hooded sweatshirt" style="background:#9b8a8c"></div></div>
  <div class="abs tile" style="left:343px"><div class="tile-art" role="img" aria-label="Light blue printed t-shirt" style="background:#a5c3d8"></div></div>
  <div class="abs tile" style="left:606px"><div class="tile-art" role="img" aria-label="Poster held up by two hands" style="background:#d9d9d9"></div></div>
  <div class="abs tile" style="left:872px"><div class="tile-art" role="img" aria-label="Vinyl record with printed sleeve" style="background:#3a3a3a"></div></div>
  <span class="abs chev" style="left:1152px">›</span>

  <section class="abs shop">
    <h2 class="abs section-title" style="top:63px">OUR <span style="color:#fff">SHOP</span></h2>
    <p class="abs section-desc" style="top:118px;width:860px;left:170px;font-size:14px">Lorem Ipsum is simply dummy text of the printing and typesetting industry. Lorem Ipsum has been the industry's standard dummy text ever since the 1500s, when an unknown printer.</p>
    <div class="abs card">
      <div class="abs card-img"><div role="img" aria-label="Set of black cinema camera lenses"></div></div>
      <div class="abs pname">PRODUCT NAME</div>
      <div class="abs stars">★★★★<span style="color:#333">★</span></div>
      <div class="abs price">$15.00 <span style="color:var(--teal);font-size:22px">🛒</span></div>
      <p class="abs pdesc">Lorem Ipsum is simply dummy text of the printing and typesetting industry. Lorem Ipsum has</p>
      <div class="abs field" style="left:442px;top:223px;width:353px">Availability <span style="float:right;color:var(--teal)">▼</span></div>
      <div class="abs field" style="left:442px;top:266px;width:172px">Arrival date</div>
      <div class="abs field" style="left:623px;top:266px;width:172px">Return date</div>
      <div class="abs book">BOOK NOW</div>
    </div>
    <div class="abs circle-arrow" style="left:33px"></div>
    <div class="abs thumb" style="left:105px;border:3px solid var(--teal)"><div role="img" aria-label="Camera lens set" style="background:#333"></div></div>
    <div class="abs thumb" style="left:272px"><div role="img" aria-label="Helmet with action camera" style="background:#444"></div></div>
    <div class="abs thumb" style="left:439px"><div role="img" aria-label="Printed t-shirt" style="background:#a5c3d8"></div></div>
    <div class="abs thumb" style="left:606px"><div role="img" aria-label="Camera drone" style="background:#ddd"></div></div>
    <div class="abs thumb" style="left:772px"><div role="img" aria-label="Camera lens front" style="background:#222;border-radius:50%"></div></div>
    <div class="abs thumb" style="left:939px"><div role="img" aria-label="Surfboard" style="background:linear-gradient(90deg,#e07a3a,#4aa3c8)"></div></div>
    <div class="abs circle-arrow" style="left:1123px"></div>
  </section>

  <h2 class="abs section-title" style="top:2106px">Latest <em>Blog</em></h2>
  <div class="abs video">
    <div class="video-img" role="img" aria-label="Video still of a surfer inside a breaking wave"></div>
    <div class="vbtn" style="top:10px"></div><div class="vbtn" style="top:58px"></div><div class="vbtn" style="top:106px"></div>
    <div style="position:absolute;left:50px;top:392px;width:520px;height:4px;background:#444"></div>
  </div>
  <div class="abs post-img" style="top:2192px" role="img" aria-label="Surfers on a beach" ><div style="width:100%;height:100%;background:linear-gradient(#9cc8e0,#d8c59a)"></div></div>
  <p class="abs post-text" style="top:2190px"><span>Lorem Ipsum is the simply dummy text of the print.</span><br>📅 Uploded by 23 Mar</p>
  <div class="abs post-img" style="top:2312px" role="img" aria-label="Surfer carrying a board"><div style="width:100%;height:100%;background:linear-gradient(#3d8fc0,#e6eef2)"></div></div>
  <p class="abs post-text" style="top:2310px"><span>Lorem Ipsum is the simply dummy text of the print.</span><br>📅 Uploded by 20 Fev</p>
  <div class="abs post-img" style="top:2432px" role="img" aria-label="Surfer riding a wave"><div style="width:100%;height:100%;background:linear-gradient(#1d6a9a,#cfe6ee)"></div></div>
  <p class="abs post-text" style="top:2430px"><span>Lorem Ipsum is the simply dummy text of the print.</span><br>📅 Uploded by 23 Jan</p>
  <div class="abs upload">UPLOAD VIDEO</div>

  <section class="abs newsletter">
    <h2>NewsLetter</h2>
    <p>Would you like to receive exclusive access to articles, white papers and our regular monthly newsletter?</p>
    <div class="abs email">Enter Email <span style="float:right;color:var(--teal)">✉</span></div>
    <div class="abs subscribe">SUBSCRIBE</div>
  </section>
</main>

<footer>
  <div class="abs footer">
    <div class="abs f-brand">Rove Reel</div>
    <p class="abs f-about">COMPANY NAME has been delivering results since we opened in YEAR.</p>
    <h4 style="left:345px">USEFULL LINKS</h4>
    <ul class="abs f-links"><li>Home</li><li>About Us</li><li>Shop</li><li>News</li><li>Faq</li><li>Bolg</li><li>Contact Us</li></ul>
    <h4 style="left:611px">LATEST BLOG</h4>
    <div class="abs f-post" style="top:82px"><i role="img" aria-label="Blog author thumbnail"></i><p>Lorem Ipsum is simply dummy text of the print.<br><small>📅 by 23 March</small></p></div>
    <div class="abs f-post" style="top:168px"><i role="img" aria-label="Blog author thumbnail"></i><p>Lorem Ipsum is simply dummy text of the print.<br><small>📅 by 23 March</small></p></div>
    <h4 style="left:874px">FOLLOW US</h4>
    <div class="abs social" style="top:94px"><i class="on"></i>Friendloop</div>
    <div class="abs social" style="top:151px"><i></i>Chirpline</div>
    <div class="abs social" style="top:210px"><i></i>Workweave</div>
  </div>
  <div class="abs bottombar">© <b>Rove Reel</b> 2017. All Rights Reserved</div>
</footer>

</body>
</html>
```